Label

I need a label designed for a bottle of water. I like the lightning bolt and the blue. But I do not want it exactly like the Zimm-ooh.

The label needs to be 9 inches by 2.5 inches.

Logo Text

Mesa Spring: Sip the Mesa

```html
<!DOCTYPE html>
<html lang="en">
<head>
<meta charset="utf-8">
<title>Mesa Spring – Bottle Label</title>
<link rel="stylesheet" href="https://fonts.googleapis.com/css2?family=Montserrat:wght@500;600;700&display=swap">
<style>
  :root {
    --sky-blue: #4f9fe0;
    --sky-light: #dfe9f7;
    --violet: #8a4fc4;
    --magenta: #c85ab8;
    --pink-mist: #e6b6dc;
    --brand-blue: #1c5fa6;
    --band-blue: #1568b8;
    --band-deep: #0f4f96;
    --white: #ffffff;
  }
  * { margin: 0; padding: 0; box-sizing: border-box; }
  html, body {
    width: 1200px;
    height: 333px;
    overflow: hidden;
    background: var(--white);
  }
  .label {
    position: relative;
    width: 1200px;
    height: 333px;
    overflow: hidden;
    font-family: "Montserrat", sans-serif;
  }
  .sky-backdrop {
    position: absolute;
    inset: 0;
    background:
      radial-gradient(ellipse 330px 190px at 600px 150px, rgba(255,255,255,0.95), rgba(255,255,255,0) 100%),
      radial-gradient(ellipse 260px 160px at 170px 140px, rgba(255,255,255,0.8), rgba(255,255,255,0) 100%),
      radial-gradient(ellipse 420px 260px at 1050px 60px, rgba(200,90,184,0.75), rgba(200,90,184,0) 100%),
      radial-gradient(ellipse 380px 220px at 40px 300px, rgba(79,159,224,0.85), rgba(79,159,224,0) 100%),
      linear-gradient(90deg, #8fb9ea 0%, var(--sky-light) 35%, #efe9f6 55%, var(--pink-mist) 75%, var(--violet) 100%);
  }
  .light-rays {
    position: absolute;
    inset: 0;
  }
  .top-strip {
    position: absolute;
    top: 0;
    left: 410px;
    width: 380px;
    height: 12px;
    background: linear-gradient(90deg, rgba(21,104,184,0), var(--band-blue) 20%, var(--band-blue) 80%, rgba(21,104,184,0));
  }
  .bottom-band {
    position: absolute;
    left: 0;
    bottom: 0;
    width: 1200px;
    height: 50px;
    background: linear-gradient(90deg, rgba(21,104,184,0) 15%, rgba(21,104,184,0.6) 32%, var(--band-deep) 45%, var(--band-deep) 55%, rgba(21,104,184,0.6) 68%, rgba(21,104,184,0) 85%);
  }
  .brand {
    position: absolute;
    left: 0;
    top: 52px;
    width: 1200px;
    text-align: center;
    color: var(--brand-blue);
    font-weight: 600;
  }
  .brand-name {
    font-size: 62px;
    line-height: 1.1;
    letter-spacing: 1px;
  }
  .brand-tagline {
    margin-top: 18px;
    font-size: 24px;
    line-height: 1.1;
    letter-spacing: 1px;
    text-transform: uppercase;
  }
  .product-type {
    position: absolute;
    left: 0;
    bottom: 6px;
    width: 1200px;
    text-align: center;
    color: var(--white);
  }
  .product-type-line1 {
    font-size: 14px;
    font-weight: 500;
    letter-spacing: 6px;
    line-height: 1.3;
  }
  .product-type-line2 {
    font-size: 18px;
    font-weight: 600;
    letter-spacing: 1.5px;
    line-height: 1.2;
  }
</style>
</head>
<body>
  <div class="label">
    <div class="sky-backdrop" role="img" aria-label="Soft sky with white clouds fading into blue, pink and violet light"></div>

    <svg class="light-rays" width="1200" height="333" viewBox="0 0 1200 333" aria-hidden="true">
      <polygon points="0,70 420,0 480,0 0,140" fill="#ffffff" opacity="0.25"/>
      <polygon points="0,333 330,333 0,230" fill="#2c7fd0" opacity="0.35"/>
      <polygon points="820,333 1200,150 1200,200 900,333" fill="#ffffff" opacity="0.18"/>
      <polygon points="760,0 1200,0 1200,40 900,0" fill="#7a3fb8" opacity="0.35"/>
      <polygon points="1000,333 1200,250 1200,333" fill="#8a4fc4" opacity="0.35"/>
    </svg>

    <div class="top-strip"></div>
    <div class="bottom-band"></div>

    <div class="brand">
      <div class="brand-name">Mesa Spring</div>
      <div class="brand-tagline">Sip the Mesa</div>
    </div>

    <div class="product-type">
      <div class="product-type-line1">NATURAL</div>
      <div class="product-type-line2">SPRING WATER</div>
    </div>
  </div>
</body>
</html>
```